Bright and beautiful business card for a coach

I'm a personal and business coach based in Perth, Australia. I need a business card that whilst subtle and elegant, will stand out and appeal on a table full of cards.

My business name is Tide Mentoring and the business card must represent the warmth and brightness implied in the name, without being gimmicky. It must have a warmth and appeal and be easy to read.

I prefer clean, minimalist designs.

It must align with the feel of my website and socials: https://www.tidementoring.com.au/
https://www.instagram.com/tidementoringau/
https://www.facebook.com/tidementoringau
Updates

Hi Designers Thank you so much for taking the time to submit designs. I wonder if I could have explained myself a little better. Most of the designs that have been submitted look rather formal and many have quite corporate looking embellishments on them (to my eye). I would like softer, warmer, more organic. I’m open to people playing about and being more abstract, using softer embellishments (e.g the line drawing flowers and grasses I’ve used in my socials) incorporating other colours from my palette or like the social icons in my email signature (in PDF), perhaps playing with size/oversize, playing with the bleed. Please don’t be constrained by what I’ve already done, it merely needs to compliment. I’m sorry if I’m not using the right words or have led you astray. I’m no designer, but I’ve done my website, socials, email signature etc all myself (my logo was a design contest) and I was really hoping for my business card to be something more creative than I could have made with a template. Reminder: No black cards/sides please. Thank you 😊

Target Market(s)

Individuals, most likely but not all female. Creative thinkers. Likely professionals.

Industry/Entity Type

Business & Personal Coach

Contact Information for Business Card

(Tide Mentoring Logo) Name: Maren Delsby; Title: Business & Personal Coach; Phone number: +61 (0)438 915307; Email: maren@tidementoring.com.au; Website: https://tidementoring.com.au; Social icons for Facebook, Instagram & LinkedIn: @tidementoringAU. Optional strapline: "A thinking partner to help you cut through the noise"

Font styles to use
Sans Serif

Colors
00AB8E
00BBA5
67D7C9
C6EFE9
E9F9F6
59FF00
82FF00
B8FF75
E3FFCB
F4FFEA
FFC000
F8CF3A
FAE287
FDF2CF
FEFAEE

Requirements
Must have
• Must align with feel of my website and socials. Must have a pop of #FFC000 (possibly whole of one side, or at least a block). Bright or white background. Easy to read.
Nice to have
• Possibly incorporate the sunshine/grass picture I have used in website and socials - will upload.
Should not have
• Must not be black or dark. Not impersonal or corporate looking.

```html
<!DOCTYPE html>
<html lang="en">
<head>
<meta charset="utf-8">
<title>Tide Mentoring – Business Card</title>
<link href="https://fonts.googleapis.com/css2?family=Great+Vibes&family=Lato:ital,wght@0,300;0,400;1,400&display=swap" rel="stylesheet">
<style>
  :root {
    --backdrop: #f4e0a0;
    --sun: #fcbf02;
    --sun-soft: #fdd24a;
    --paper: #ffffff;
    --bronze: #b8701f;
    --mint: #a9d5c7;
    --mint-deep: #b0d6c8;
    --white: #ffffff;
  }
  * { margin: 0; padding: 0; box-sizing: border-box; }
  html, body {
    width: 1200px; height: 1091px; overflow: hidden;
    background: var(--backdrop);
  }
  .canvas { position: relative; width: 1200px; height: 1091px; }

  .card { position: absolute; width: 695px; height: 398px; overflow: hidden; }

  /* Front */
  .card-front { left: 129px; top: 174px; background: var(--sun); z-index: 2; }
  .front-decor {
    position: absolute;
    background: radial-gradient(ellipse at center, var(--sun-soft) 0%, rgba(253,210,74,0.55) 45%, rgba(252,191,2,0) 72%);
  }
  .front-decor--top { left: -60px; top: -80px; width: 420px; height: 300px; }
  .front-decor--bottom { right: -40px; bottom: -70px; width: 460px; height: 330px; }
  .brand-name {
    position: absolute; left: 0; right: 0; top: 168px;
    text-align: center;
    font-family: "Lato", sans-serif; font-weight: 400;
    font-size: 46px; letter-spacing: 3px;
    color: var(--white);
  }

  /* Back */
  .card-back { left: 374px; top: 512px; background: var(--paper); z-index: 1; }
  .back-decor {
    position: absolute; right: 0; bottom: 0; width: 380px; height: 190px;
    background: radial-gradient(ellipse at 80% 100%, var(--mint-deep) 0%, rgba(176,214,200,0.6) 40%, rgba(176,214,200,0) 72%);
  }
  .contact { position: absolute; left: 36px; top: 90px; }
  .person-name {
    font-family: "Great Vibes", cursive;
    font-size: 62px; line-height: 1; color: var(--bronze);
  }
  .person-title {
    margin-top: 6px;
    font-family: "Lato", sans-serif; font-weight: 300;
    font-size: 27px; color: var(--mint); letter-spacing: 0.5px;
  }
  .details { list-style: none; margin-top: 12px; font-family: "Lato", sans-serif; font-size: 19px; color: var(--mint); }
  .details li { display: flex; align-items: center; height: 29px; }
  .details svg { width: 24px; height: 20px; margin-right: 8px; fill: var(--bronze); }
  .details .web { font-style: italic; }
  .social { display: flex; gap: 8px; margin-top: 10px; }
  .social span { width: 22px; height: 22px; border-radius: 50%; background: var(--bronze); }
</style>
</head>
<body>
<main class="canvas">
  <section class="card card-front">
    <div class="front-decor front-decor--top" role="img" aria-label="Soft hand-drawn leaf and grass shapes in pale yellow"></div>
    <div class="front-decor front-decor--bottom" role="img" aria-label="Soft hand-drawn leaf and grass shapes in pale yellow"></div>
    <p class="brand-name">Tide Mentoring</p>
  </section>

  <section class="card card-back">
    <div class="back-decor" role="img" aria-label="Hand-drawn leaf and grass shapes in mint green"></div>
    <div class="contact">
      <h1 class="person-name">Maren Delsby</h1>
      <p class="person-title">Business &amp; Personal Coach</p>
      <ul class="details">
        <li>
          <svg viewBox="0 0 24 18" aria-hidden="true"><path d="M0 0h24v3L12 10 0 3z"/><path d="M0 5l12 7 12-7v13H0z"/></svg>
          maren@tidementoring.com.au
        </li>
        <li>
          <svg viewBox="0 0 24 24" aria-hidden="true"><path d="M6.6 10.8a15.1 15.1 0 0 0 6.6 6.6l2.2-2.2c.3-.3.7-.4 1-.2 1.1.4 2.3.6 3.6.6.6 0 1 .4 1 1V20c0 .6-.4 1-1 1A17 17 0 0 1 3 4c0-.6.4-1 1-1h3.5c.6 0 1 .4 1 1 0 1.3.2 2.5.6 3.6.1.3 0 .7-.2 1z"/></svg>
          +61 (0)438 915307
        </li>
        <li class="web">https://tidementoring.com.au</li>
        <li>@tidementoringAU</li>
      </ul>
      <div class="social" aria-label="Social profiles"><span></span><span></span><span></span></div>
    </div>
  </section>
</main>
</body>
</html>
```